New Basketball Sports Agency need webpage design

We are a ZEMO/KXV Sports agency looking for a new Webpage design. We currently have a site @ www.pvtcourtwork.com, and looking for someone to redesign the site.. We are also looking to redo the LOGO as well. PVT will begin its Brightrun camps also, and would like a page to promote and sign up for camp. I already have tallywise, but not sure how to add to site. Site must include:

Page for Agency updates, Client profiles, page for admin, camp registration page, flash photos, and able to filter news updates from gryphonwire, and TRKO sites.

Target Market(s)

European basketball clubs, USA Teams, Basketball Players, Sports Agents, Sports Directors General Managers,

Industry/Entity Type

News

```html
<!DOCTYPE html>
<html lang="en">
<head>
<meta charset="utf-8">
<title>PVT Basketball – Home</title>
<link href="https://fonts.googleapis.com/css2?family=Arimo:ital,wght@0,400;0,700;1,700&family=Raleway:wght@500;700;800&family=Sorts+Mill+Goudy&display=swap" rel="stylesheet">
<style>
:root{
  --ink:#000;
  --orange:#f7801f;
  --orange-light:#fb9a3f;
  --orange-dark:#e46a10;
  --leather:#4a1e0c;
  --leather-deep:#2a0f05;
  --panel:#0c0c0c;
  --panel-line:#2a2a2a;
  --text:#d6d6d6;
  --muted:#a9a9a9;
  --white:#fff;
  --frame:#bdbdbd;
  --footer:#161616;
}
*{box-sizing:border-box;margin:0;padding:0}
html,body{width:1034px;height:1200px;overflow:hidden;background:var(--ink)}
.page{
  position:relative;width:1034px;height:1200px;overflow:hidden;
  font-family:"Arimo",Arial,sans-serif;color:var(--text);
  background:
    radial-gradient(ellipse 260px 420px at 40px 470px,rgba(110,45,18,.75),transparent 70%),
    radial-gradient(ellipse 300px 520px at 1010px 380px,rgba(120,50,20,.8),transparent 70%),
    radial-gradient(ellipse 700px 300px at 517px 620px,rgba(70,28,10,.55),transparent 70%),
    var(--ink);
}
.abs{position:absolute}
.brand{left:110px;top:26px;display:flex;align-items:center;gap:12px}
.brand-dot{width:54px;height:54px;border-radius:50%;background:var(--orange)}
.brand-name{font-family:"Raleway",sans-serif;font-weight:800;font-size:34px;color:var(--orange);line-height:1;letter-spacing:.5px}
.hoop-art{left:866px;top:0;width:88px;height:124px;border-radius:0 0 44px 44px;
  background:linear-gradient(180deg,#3a3a3a,#1a1a1a 55%,#b4532a)}
.social-btn{top:83px;height:27px;border-radius:6px;border:1px solid #777;
  background:linear-gradient(#5a5a5a,#262626);color:var(--white);
  font:700 11px "Raleway",sans-serif;display:flex;align-items:center;justify-content:center}
.nav{left:95px;top:131px;width:843px;height:39px;border-radius:10px;
  background:linear-gradient(var(--orange-light),var(--orange) 50%,var(--orange-dark))}
.nav-home{left:126px;top:126px;width:87px;height:50px;background:linear-gradient(#2a2a2a,#000);
  border:1px solid #333}
.nav-item{top:142px;font:500 13px "Raleway",sans-serif;color:var(--white);transform:translateX(-50%);white-space:nowrap}
.slider{left:102px;top:200px;width:831px;height:316px;border:4px solid var(--frame);
  background:radial-gradient(ellipse at 60% 40%,#4b3d55,#16131c 70%)}
.arrow{top:342px;width:28px;height:34px;background:linear-gradient(#eee,#9a9a9a);
  color:#111;font:700 16px Arial,sans-serif;display:flex;align-items:center;justify-content:center}
.welcome{left:103px;top:546px;width:826px;height:285px;border:1px solid var(--panel-line);border-radius:5px;
  background:linear-gradient(rgba(12,12,12,.92),rgba(20,20,20,.85))}
.serif{font-family:"Sorts Mill Goudy",Georgia,serif;font-weight:400}
.welcome h1{position:absolute;left:24px;top:17px;font-size:26px;color:var(--white)}
.accent{color:var(--orange)}
.dotted{position:absolute;left:16px;right:16px;top:56px;border-top:1px dotted #3c3c3c}
.photo-tilt{left:112px;top:624px;width:210px;height:160px;transform:rotate(-3deg);
  background:rgba(120,120,120,.25)}
.photo{border:1px solid #555}
.welcome-photo{left:123px;top:638px;width:191px;height:138px;
  background:linear-gradient(160deg,#1c2a44,#a5241c 55%,#0f0f14)}
.welcome-copy{left:361px;top:632px;width:527px;font-size:11px;line-height:17.2px;text-align:justify;color:var(--text)}
.welcome-copy .lead{font-weight:700;font-style:italic;color:var(--white)}
.welcome-copy p+p{margin-top:17px}
.news-title{left:102px;top:856px;font-size:24px;color:var(--orange)}
.news-head{left:105px;top:900px;font-size:20px;color:var(--white);white-space:nowrap}
.news-photo{left:104px;top:945px;width:93px;height:138px;border:2px solid #ddd;
  background:linear-gradient(#d9d2c2,#5a3d8c 55%,#c9bfa8)}
.news-copy{left:213px;top:947px;width:429px;font-size:10.5px;line-height:15.5px;text-align:justify;color:var(--muted)}
.video{left:682px;top:894px;width:246px;height:201px;background:#111}
.footer{left:0;top:1125px;width:1034px;height:75px;background:var(--footer);border-top:1px solid #2b2b2b}
.footer-links{left:107px;top:1144px;font-size:11px;color:#cfcfcf;white-space:nowrap;word-spacing:1px}
.footer-links span{color:#888;margin:0 10px}
.follow{left:785px;top:1139px;font:700 9.5px "Arimo",sans-serif;color:#bbb;white-space:nowrap}
.follow b{color:var(--white);margin-left:6px}
.copyright{left:0;width:1034px;top:1177px;text-align:center;font-size:11px;color:#cfcfcf}
</style>
</head>
<body>
<div class="page">

  <header>
    <div class="abs brand"><span class="brand-dot"></span><span class="brand-name">PVT Basketball</span></div>
    <div class="abs social-btn" style="left:670px;width:84px">Friendloop</div>
    <div class="abs social-btn" style="left:765px;width:90px">Chirpline</div>
    <div class="abs hoop-art" role="img" aria-label="Basketball hoop with net and ball"></div>
  </header>

  <nav>
    <div class="abs nav"></div>
    <div class="abs nav-home"></div>
    <a class="abs nav-item" style="left:167px">Home</a>
    <a class="abs nav-item" style="left:272px">Clients</a>
    <a class="abs nav-item" style="left:443px">Basketball Bootcamp</a>
    <a class="abs nav-item" style="left:655px">High School Services</a>
    <a class="abs nav-item" style="left:827px">More...</a>
  </nav>

  <section>
    <div class="abs slider" role="img" aria-label="Player rising for a dunk under arena lights"></div>
    <div class="abs arrow" style="left:99px">&#10095;</div>
    <div class="abs arrow" style="left:909px">&#10094;</div>
  </section>

  <section>
    <div class="abs welcome">
      <h1 class="serif">Welcome to <span class="accent">Palmetto Valley Training</span></h1>
      <div class="dotted"></div>
    </div>
    <div class="abs photo-tilt"></div>
    <div class="abs photo welcome-photo" role="img" aria-label="Player hanging on the rim after a dunk"></div>
    <div class="abs welcome-copy">
      <p><span class="lead">Lorem ipsum dolor sit amet, consectetuer adipiscing elit, sed diam nonummy nibh euismod tincidunt</span> ut laoreet dolore magna aliquam erat volutpat. Ut wisi enim ad minim veniam, quis nostrud exerci tation ullam-corper suscipit lobortis nisl ut aliquip ex ea commodo consequat. Duis autem vel eum iriure dolor in hendrerit in vulputate velit esse molestie consequat, vel illum dolore eu feugiat nulla facilisis at vero eros et accumsan et iusto odio dignissim qui blandit praesent luptatum zzril delenit augue duis dolore te feugait nulla facilisi.Epsum factorial non deposit quid pro quo hic escorol.</p>
      <p>Olypian quarrels et gorilla congolium sic ad nauseum. Souvlaki ignitus carborundum e pluribus unum. Defacto lingo est igpay atinlay. Marquee selectus non provisio incongruous feline nolo contendre. Gratuitous octopus niacin, sodium glutimate. Quote meon an estimate et non interruptus stadium.</p>
    </div>
  </section>

  <section>
    <h2 class="abs news-title serif">Latest News</h2>
    <h3 class="abs news-head serif">PVT lands Nations Top Freethrow Shooting PG Dorian Welles</h3>
    <div class="abs news-photo" role="img" aria-label="Guard dribbling in a purple uniform"></div>
    <p class="abs news-copy">The 6'2" PG/SG Marcus Tillery just signed a representation agreement with Palmetto Valley Training. Marc is a product of Brookhaven Hollis University under coach Glen Ostrow. He's a player with definate KXV athletic potential... Uses his quickness and excellent handle to change directions and breakdown the defense, Shines in the open floor where he attacks the basket and uses his speed, momentum and strength to finish on the break ... Shows steady body control when the 2012 NCAB Division I the gryphonwire Summer league in Vegas on July 16th at The Desert Ridge State University Recreation Center, located right next to Ridgeline Arena where KXV Summer League will be playing. Player BIO</p>
    <svg class="abs video" width="246" height="201" viewBox="0 0 246 201">
      <rect width="246" height="201" fill="#111"/>
      <circle cx="224" cy="10" r="4" fill="#ccc"/>
      <circle cx="237" cy="10" r="4" fill="#ccc"/>
      <rect x="1" y="22" width="244" height="136" fill="#8a6e4e" role="img" aria-label="Game footage of a college basketball match"/>
      <rect x="1" y="22" width="244" height="136" fill="url(#court)"/>
      <defs><linearGradient id="court" x1="0" y1="0" x2="0" y2="1"><stop offset="0" stop-color="#6b6a6e"/><stop offset="1" stop-color="#b98a57"/></linearGradient></defs>
      <rect x="102" y="78" width="42" height="30" rx="6" fill="#1b1b1b" opacity=".85"/>
      <path d="M118 86 L118 100 L130 93 Z" fill="#fff"/>
      <rect x="1" y="158" width="244" height="43" fill="#1a1a1a"/>
      <rect x="4" y="167" width="238" height="4" fill="#d42020"/>
      <circle cx="6" cy="169" r="4" fill="#eee"/>
      <path d="M16 183 L16 191 L23 187 Z" fill="#bbb"/>
      <rect x="37" y="184" width="4" height="6" fill="#bbb"/>
      <text x="56" y="190" font-family="Arimo,sans-serif" font-size="7" fill="#ccc">0:00</text>
      <text x="196" y="190" font-family="Arimo,sans-serif" font-size="7" fill="#ccc">Clipstream</text>
    </svg>
  </section>

  <footer>
    <div class="abs footer"></div>
    <div class="abs footer-links">Home<span>|</span>Clients<span>|</span>Basketball Bootcamp<span>|</span>High School Services<span>|</span>More...</div>
    <div class="abs follow">Follow Us on :<b>Friendloop</b><b>Worknet</b><b>Chirpline</b></div>
    <div class="abs copyright">Copyright (C) pvtcourtwork.com. 2013.&nbsp; All Rights Reserved</div>
  </footer>

</div>
</body>
</html>
```